Bottle label design for a mulberry brandy

Please create a label design for a mulberry brandy. The registered brand name is "Kolvat"
The brandy will be produced in Armenia from 100% mulberry.
Color of the product: transparent.
The product will be sold worldwide. The price will be between 30 and 50 USD. So the product will be in premium category.
Therefore we need a solid design, appropriate to the product price category. The design, however, needs to be modern and optimistic.
You can have mulberries on the label or not have, it is up to you.
We have chosen for the product some bottle types, the links to the available bottles you can find in the attachment. Ideally you show a picture of your label on the bottle you selected.

Target Market(s)

worldwide

```html
<!DOCTYPE html>
<html lang="en">
<head>
<meta charset="utf-8">
<title>Kolvat – Mulberry Brandy Label</title>
<link rel="stylesheet" href="https://fonts.googleapis.com/css2?family=Cormorant+Garamond:wght@400;700&family=Great+Vibes&display=swap">
<style>
  :root {
    --ink: #000000;
    --paper: #ffffff;
    --fruit-light: #e6e6e6;
    --fruit-dark: #2a2a2a;
  }
  html, body {
    margin: 0;
    padding: 0;
    overflow: hidden;
    background: var(--paper);
  }
  .label {
    position: relative;
    width: 1010px;
    height: 1200px;
    background: var(--paper);
    overflow: hidden;
    font-family: "Cormorant Garamond", Georgia, serif;
  }
  .label__diagonal {
    position: absolute;
    inset: 0;
    width: 1010px;
    height: 1200px;
  }
  .label__diagonal polygon {
    fill: var(--ink);
  }
  .brand-name {
    position: absolute;
    left: 322px;
    top: 92px;
    margin: 0;
    font-family: "Great Vibes", cursive;
    font-weight: 400;
    font-size: 190px;
    line-height: 1;
    color: var(--ink);
    white-space: nowrap;
  }
  .product-type {
    position: absolute;
    left: 365px;
    top: 322px;
    margin: 0;
    font-size: 50px;
    line-height: 1;
    color: var(--ink);
    white-space: nowrap;
    font-variant-numeric: oldstyle-nums;
  }
  .product-type strong {
    font-weight: 700;
  }
  .fruit-artwork {
    position: absolute;
    left: 238px;
    top: 508px;
    width: 593px;
    height: 323px;
    border-radius: 160px;
    background: linear-gradient(135deg, var(--fruit-light) 0%, var(--fruit-light) 50%, var(--fruit-dark) 50%, var(--fruit-dark) 100%);
  }
  .origin,
  .volume {
    position: absolute;
    margin: 0;
    color: var(--paper);
    line-height: 1;
    white-space: nowrap;
  }
  .origin {
    left: 125px;
    top: 982px;
    font-size: 36px;
    font-weight: 700;
  }
  .volume {
    left: 246px;
    top: 1046px;
    font-size: 36px;
    font-weight: 700;
    font-variant-numeric: oldstyle-nums;
  }
</style>
</head>
<body>
  <main class="label">
    <svg class="label__diagonal" viewBox="0 0 1010 1200" aria-hidden="true">
      <polygon points="0,0 962,1200 0,1200"/>
    </svg>

    <h1 class="brand-name">Kolvat</h1>
    <p class="product-type">100% <strong>mulberry</strong> brandy</p>

    <div class="fruit-artwork" role="img" aria-label="Silhouette of two mulberries on a stem with a serrated leaf, crossing the diagonal split"></div>

    <p class="origin">produced in Armenia</p>
    <p class="volume">700ml</p>
  </main>
</body>
</html>
```